Wedding and event Photography company.

We need a business card design for a photography company based in Singapore named TamKeza. Our core service offering is wedding photojournalism. We would like to see minimalistic designs that use the colour white. The final design should communicate a sense of ease and reliability.

The attached are a couple of visual reference which i found over the web, i hope it will helps.

Project Brief Update (14th July 2014):
- Please refrain from using any images from the website for the design. The laws and regulations over here does not allow me to distribute my client's images. Thanks!

Target Market(s)

Young and middle aged adults aged 24 - 38. With money to spend =D

Industry/Entity Type

Business

Contact Information for Business Card

Name: Dev Lunor
Designation: Head Photographer
Mobile: +65 81749026
Email: jun@tamkeza.example
Website: www.tamkeza.example

Font styles to use
Other font styles liked:
• Baskerville URW

Colors

Designer to choose colors to be used in the design.

Requirements
Must have
• Must include:
• - The brand TamKeza
• - The logo attached
• - Please help to place the brand TamKeza with the logo according to your preferences.
• - Services
• - Wedding Photography
• - Portraiture
• - Photojournalism
Nice to have
• Looking forward to an elegant and simple design. Please see attached examples!
• Please use Serif Fonts
Should not have
• Please refrain from using dark tones for the majority of the design.
• Please refrain from letterpress and embossing.

```html
<!DOCTYPE html>
<html lang="en">
<head>
<meta charset="utf-8">
<title>TamKeza — Business Card</title>
<link href="https://fonts.googleapis.com/css2?family=Libre+Baskerville:wght@400;700&display=swap" rel="stylesheet">
<style>
  :root {
    --backdrop: #d9d9d7;
    --card: #f4f4f1;
    --ink: #1b1b1b;
    --shadow: rgba(0, 0, 0, 0.16);
  }
  * { box-sizing: border-box; margin: 0; padding: 0; }
  html, body {
    width: 1200px;
    height: 1200px;
    overflow: hidden;
    background: var(--backdrop);
  }
  .canvas {
    position: relative;
    width: 1200px;
    height: 1200px;
    font-family: "Libre Baskerville", "Baskerville", serif;
    color: var(--ink);
  }
  .card {
    position: absolute;
    width: 840px;
    height: 480px;
    background: var(--card);
    box-shadow: 0 10px 26px var(--shadow);
    display: flex;
    flex-direction: column;
    align-items: center;
    text-align: center;
  }
  .card--front { left: 280px; top: 100px; justify-content: center; }
  .card--back  { left: 80px;  top: 620px; justify-content: center; }

  .brand-mark {
    display: flex;
    align-items: center;
    gap: 14px;
    font-size: 46px;
    font-weight: 400;
    letter-spacing: 2px;
    margin-bottom: 26px;
  }
  .brand-mark__dot {
    width: 12px;
    height: 12px;
    border-radius: 50%;
    background: var(--ink);
  }
  .brand-line {
    font-size: 19px;
    letter-spacing: 9px;
    text-transform: uppercase;
    margin-bottom: 36px;
  }
  .website {
    font-size: 15px;
    letter-spacing: 4px;
  }

  .person-name {
    font-size: 25px;
    letter-spacing: 5px;
    text-transform: uppercase;
  }
  .person-role {
    font-size: 17px;
    letter-spacing: 5px;
    text-transform: uppercase;
    margin-top: 6px;
    margin-bottom: 26px;
  }
  .contact {
    font-size: 17px;
    letter-spacing: 3px;
    line-height: 1.75;
  }
  .divider {
    width: 26px;
    height: 3px;
    background: var(--ink);
    margin: 24px 0 26px;
  }
  .services {
    display: flex;
    align-items: center;
    gap: 22px;
    font-size: 17px;
    letter-spacing: 3px;
    list-style: none;
  }
  .services__sep {
    width: 7px;
    height: 7px;
    border-radius: 50%;
    background: var(--ink);
  }
</style>
</head>
<body>
<main class="canvas">
  <section class="card card--front" aria-label="Card front">
    <div class="brand-mark">
      <span class="brand-mark__dot"></span>
      <span class="brand-mark__name">TamKeza</span>
    </div>
    <p class="brand-line">The Brand TamKeza</p>
    <p class="website">www.tamkeza.example</p>
  </section>

  <section class="card card--back" aria-label="Card back">
    <h1 class="person-name">Dev Lunor</h1>
    <p class="person-role">Head Photographer</p>
    <p class="contact">
      +65 81749026<br>
      jun@tamkeza.example | www.tamkeza.example
    </p>
    <div class="divider"></div>
    <ul class="services">
      <li>Wedding Photography</li>
      <li class="services__sep" aria-hidden="true"></li>
      <li>Portraiture</li>
      <li class="services__sep" aria-hidden="true"></li>
      <li>Photojournalism</li>
    </ul>
  </section>
</main>
</body>
</html>
```